Flyer Design Project

Training and Consulting Flyer

I attached a document that contained the wording for the flyer as well as the logo.

Target Market(s)

Little Compass agencies and grantees

Industry/Entity Type

Training

Font styles to use
Sans Serif

Colors
e667a6
eda3c7
a54499
b768aa
f9d9e8

Requirements
Must have
• Words provided on attachment
Nice to have
• Graphics that are related to adult training/learning and consulting

```html
<!DOCTYPE html>
<html lang="en">
<head>
<meta charset="utf-8">
<title>Ivorywell Consultants – Flyer</title>
<link rel="stylesheet" href="https://fonts.googleapis.com/css2?family=Bebas+Neue&family=Source+Sans+3:ital,wght@0,400;0,600;0,700;1,400;1,700&display=swap">
<style>
  :root {
    --backdrop: #404040;
    --paper: #ffffff;
    --magenta: #b01e6e;
    --ink: #111111;
    --body-ink: #1d1d1d;
    --footer: #202020;
    --photo-a: #d9cfc8;
    --photo-b: #8c7b70;
    --photo-c: #c9d0d6;
    --photo-d: #6f7a86;
  }
  * { box-sizing: border-box; margin: 0; padding: 0; }
  html, body {
    width: 1200px; height: 1200px; overflow: hidden;
    background: var(--backdrop);
  }
  .flyer {
    position: absolute; left: 194px; top: 76px;
    width: 811px; height: 1050px;
    background: var(--paper); overflow: hidden;
    font-family: "Source Sans 3", sans-serif;
  }
  .brand {
    position: absolute; left: 46px; top: 44px;
    display: flex; align-items: center; gap: 14px;
  }
  .brand-dot {
    width: 24px; height: 24px; border-radius: 50%;
    background: var(--magenta);
  }
  .brand-name {
    font-family: "Bebas Neue", sans-serif;
    font-size: 38px; line-height: 36px; color: var(--ink);
    letter-spacing: .5px;
    border-left: 1.5px solid var(--ink); padding-left: 10px;
  }
  .tagline {
    position: absolute; left: 66px; top: 128px;
    font-size: 14px; letter-spacing: .4px; color: var(--ink);
  }
  .pillars {
    position: absolute; left: 38px; top: 163px;
    width: 207px; height: 190px;
    background: var(--magenta);
    border-radius: 22px 34px 0 34px;
    padding: 24px 0 0 20px;
    font-family: "Bebas Neue", sans-serif;
    color: #fff; font-size: 45px; line-height: 45px;
  }
  .photo { position: absolute; }
  .photo-team {
    left: 277px; top: 42px; width: 445px; height: 312px;
    background: linear-gradient(135deg, var(--photo-a), var(--photo-b));
    border-radius: 0 0 40px 0;
  }
  .photo-class {
    left: 42px; top: 370px; width: 203px; height: 188px;
    background: linear-gradient(135deg, var(--photo-c), var(--photo-d));
    border-radius: 26px 0 26px 0;
  }
  .headline {
    position: absolute; left: 278px; top: 380px;
    font-family: "Bebas Neue", sans-serif; font-weight: 400;
    font-size: 46px; line-height: 1; color: var(--magenta);
    letter-spacing: .2px; white-space: nowrap;
  }
  .intro {
    position: absolute; left: 279px; top: 428px; width: 470px;
    font-size: 24px; line-height: 34px; font-weight: 700; color: var(--ink);
    white-space: nowrap;
  }
  .intro .focus { color: var(--magenta); display: block; }
  .services {
    position: absolute; left: 46px; top: 590px; width: 690px;
    list-style: none;
  }
  .services li {
    position: relative; padding-left: 20px; margin-bottom: 12px;
    font-size: 17px; line-height: 22.4px; color: var(--body-ink);
  }
  .services li svg {
    position: absolute; left: 0; top: 6px; width: 13px; height: 11px;
  }
  .signoff {
    position: absolute; left: 46px; top: 920px;
    font-size: 35px; font-weight: 700; font-style: italic; color: var(--magenta);
  }
  .footer {
    position: absolute; left: 0; top: 982px; width: 811px; height: 68px;
    background: var(--footer);
    display: flex; align-items: center; gap: 26px; padding-left: 20px;
    color: #fff; font-size: 14.5px; font-weight: 600;
  }
  .footer span { display: flex; align-items: center; gap: 10px; }
  .footer svg { width: 13px; height: 13px; fill: var(--magenta); }
  .swoosh { position: absolute; left: 0; top: 0; width: 811px; height: 1050px; pointer-events: none; }
</style>
</head>
<body>
<main class="flyer">
  <div class="brand">
    <div class="brand-dot"></div>
    <div class="brand-name">Ivorywell<br>Consultants</div>
  </div>
  <div class="tagline">TOGETHER WE CAN</div>

  <div class="pillars">Knowledge.<br>Analysis.<br>Statistics.</div>

  <div class="photo photo-team" role="img" aria-label="Photo of a cheering group of professionals raising their arms"></div>
  <div class="photo photo-class" role="img" aria-label="Photo of adult learners in a training room giving thumbs up"></div>

  <h1 class="headline">Health Consultants &amp; Groups</h1>
  <p class="intro">Innovative approaches to meeting the<br>5 year funding measures in the<br>content area of
    <span class="focus">Health, Nutrition, Oral Health &amp; Safety</span></p>

  <ul class="services">
    <li><svg viewBox="0 0 13 11"><path d="M0 0L13 5.5L0 11L3 5.5Z" fill="var(--magenta)"/></svg>Ivorywell Consultants has embarked on a new methodology designed to ensure<br>programmes meet total requirments as prescribed under the <i>Little Compass Programme</i>.</li>
    <li><svg viewBox="0 0 13 11"><path d="M0 0L13 5.5L0 11L3 5.5Z" fill="var(--magenta)"/></svg>Let us manage your health programme through remote and offsite measures to ensure<br>total compliance and strategic methodology toward quality service approaches.</li>
    <li><svg viewBox="0 0 13 11"><path d="M0 0L13 5.5L0 11L3 5.5Z" fill="var(--magenta)"/></svg>Let us provide consultants to mentor your health manager nutrition content specialist<br>facility/safety manager. These support consultants are advanced level academias in their<br>specialised areas of focus.</li>
    <li><svg viewBox="0 0 13 11"><path d="M0 0L13 5.5L0 11L3 5.5Z" fill="var(--magenta)"/></svg>Let us provide Mock Reviews for your programme designed to assist management staff<br>in Focus I, Focus II, review strategies for 2018.</li>
    <li><svg viewBox="0 0 13 11"><path d="M0 0L13 5.5L0 11L3 5.5Z" fill="var(--magenta)"/></svg>Let us provide T/TA for any new health nutrition, safety staff to ensure they are fully<br>prepared to perform their job duties at their highest level of management<br>approaches.</li>
  </ul>

  <div class="signoff">Dana Morrow, CEO</div>

  <footer class="footer">
    <span><svg viewBox="0 0 13 13"><path d="M0 3h13v8H0z M0 3l6.5 4L13 3" /></svg>hello@ivorywellconsult.com</span>
    <span><svg viewBox="0 0 13 13"><path d="M2.5 0.5l2.3 2.8-1.3 1.7c.8 1.8 2.3 3.3 4.2 4.2l1.7-1.3 2.8 2.3-1.4 2.3C5.5 12.3.7 7.5.2 1.9z"/></svg>(555) 014-2290</span>
    <span><svg viewBox="0 0 13 13"><path d="M6.5 0C4 0 2.2 1.9 2.2 4.3 2.2 7.4 6.5 13 6.5 13s4.3-5.6 4.3-8.7C10.8 1.9 9 0 6.5 0zm0 6a1.7 1.7 0 110-3.4 1.7 1.7 0 010 3.4z"/></svg>P.O Box 482 Fairbrook, GA 30099</span>
  </footer>

  <svg class="swoosh" viewBox="0 0 811 1050" aria-hidden="true">
    <path d="M738 0 C786 150 786 500 773 640 C759 800 720 930 666 1050 L811 1050 L811 0 Z" fill="var(--magenta)"/>
  </svg>
</main>
</body>
</html>
```